Flat bootstrap design for existing site

I'm looking for a modern flat design based around an existing logo. This has to be a custom design (no external templates), and implemented into a bootstrap framework.

The logo is attached as 2 versions - choose whichever you want, that flows better with whatever design you choose.

Added screenshots of the existing site (currently using the default bootstrap layouts). Please make your designs around those pages in the screenshots (i.e. the homepage only has the postal code input and the header). The active page has 3 screenshots, because I wanted to illustrate the other states that would be visible (in the table rows).

This is a moving/junk removal website, just for some context.

Here's some example websites (flat designs) that I like, just to give you an idea of what I'm after.

https://www.plivoterra.com/
https://damsoqua.com/
https://trevalin.com/
https://morkadelphi.com/en/

Coding

Coded - Design and coding required

Number of Pages Required

5+ page

Colors

Designer to choose colors to be used in the design.

Requirements
Must have
• It must be a modern/simple flat design, that is built around the existing logo (attached).
• It has to be implemented using bootstrap.

```html
<!DOCTYPE html>
<html lang="en">
<head>
<meta charset="utf-8">
<title>Haulwick – Login</title>
<link rel="stylesheet" href="https://fonts.googleapis.com/css2?family=Lato:wght@400;700;900&display=swap">
<style>
  :root {
    --sky: #38cdff;
    --sky-tile: #4fc9f2;
    --panel: #76dbfc;
    --page: #f4f4f4;
    --white: #ffffff;
    --hint: #93dcf6;
    --action: #f46524;
  }
  * { box-sizing: border-box; margin: 0; padding: 0; }
  html, body {
    width: 1200px;
    height: 667px;
    overflow: hidden;
  }
  body {
    position: relative;
    background: var(--page);
    font-family: "Lato", sans-serif;
  }
  .site-header {
    position: absolute;
    left: 0; top: 0;
    width: 1200px;
    height: 89px;
    background: var(--sky);
  }
  .brand {
    position: absolute;
    left: 78px; top: 0;
    width: 178px;
    height: 89px;
    background: var(--sky-tile);
    display: flex;
    align-items: center;
    justify-content: center;
    color: var(--white);
    font-weight: 900;
    font-size: 24px;
    letter-spacing: 0.5px;
    text-decoration: none;
  }
  .main-nav a {
    position: absolute;
    top: 31px;
    height: 32px;
    line-height: 32px;
    color: var(--white);
    font-weight: 700;
    font-size: 15.5px;
    text-decoration: none;
    white-space: nowrap;
  }
  .main-nav .is-current {
    border: 2px solid var(--white);
    padding: 0 9px;
    line-height: 28px;
  }
  .nav-book { left: 599px; width: 69px; }
  .nav-how { left: 690px; }
  .nav-driver { left: 843px; }
  .nav-login { left: 1012px; }

  .login-card {
    position: absolute;
    left: 409px; top: 190px;
    width: 382px;
    height: 328px;
    background: var(--panel);
    border-radius: 5px;
  }
  .login-field {
    position: absolute;
    left: 43px;
    width: 295px;
    height: 52px;
    border: none;
    border-radius: 4px;
    background: var(--white);
    padding: 0 17px;
    font-family: "Lato", sans-serif;
    font-weight: 700;
    font-size: 15px;
    color: #333;
  }
  .login-field::placeholder { color: var(--hint); }
  .field-email { top: 68px; }
  .field-password { top: 133px; }
  .login-button {
    position: absolute;
    left: 43px; top: 200px;
    width: 295px;
    height: 52px;
    border: none;
    border-radius: 4px;
    background: var(--action);
    color: var(--white);
    font-family: "Lato", sans-serif;
    font-weight: 700;
    font-size: 20px;
  }
</style>
</head>
<body>
  <header class="site-header">
    <a class="brand" href="#">HAULWICK</a>
    <nav class="main-nav">
      <a class="nav-book is-current" href="#">BOOK</a>
      <a class="nav-how" href="#">HOW IT WORKS</a>
      <a class="nav-driver" href="#">BECOME A DRIVER</a>
      <a class="nav-login" href="#">LOGIN</a>
    </nav>
  </header>

  <main>
    <form class="login-card" action="#">
      <input class="login-field field-email" type="email" placeholder="Email address" aria-label="Email address">
      <input class="login-field field-password" type="password" placeholder="Password" aria-label="Password">
      <button class="login-button" type="submit">LOGIN</button>
    </form>
  </main>
</body>
</html>
```